Velmarine - Mechanic/Collision Center Business Card

We're looking for a business card design for our mechanic/ collision repair shop.

Can be with colours or monochromatic.

See the attached files.

Many thanks

```html
<!DOCTYPE html>
<html lang="en">
<head>
<meta charset="utf-8">
<title>Velmarine Business Card</title>
<link href="https://fonts.googleapis.com/css2?family=Roboto:wght@400;900&display=swap" rel="stylesheet">
<style>
  :root {
    --backdrop: #444444;
    --card-white: #ffffff;
    --brand-blue: #1f9fdb;
    --accent-blue: #1e9bd7;
    --ink: #2a2a2a;
    --brand-ink: #1d1d1f;
  }
  * { margin: 0; padding: 0; box-sizing: border-box; }
  html, body {
    width: 1200px; height: 800px; overflow: hidden;
    background: var(--backdrop);
    font-family: "Roboto", Arial, sans-serif;
  }
  .card {
    position: absolute;
    top: 292px;
    width: 438px;
    height: 251px;
    overflow: hidden;
  }
  .card--front { left: 147px; background: var(--card-white); }
  .card--back { left: 612px; background: var(--brand-blue); }

  .brand-name {
    position: absolute;
    display: flex;
    align-items: center;
    gap: 8px;
    font-weight: 900;
    font-size: 30px;
    letter-spacing: 0.5px;
    color: var(--brand-ink);
  }
  .brand-name .mark {
    width: 16px; height: 16px;
    background: var(--brand-blue);
  }
  .card--back .brand-name .mark { background: var(--card-white); }
  .card--front .brand-name { left: 15px; top: 48px; }
  .card--back .brand-name { right: 16px; top: 180px; }

  .company {
    position: absolute; left: 15px; top: 127px;
    color: var(--accent-blue);
    font-size: 13.5px;
    font-weight: 400;
  }
  .address {
    position: absolute; left: 15px; top: 145px;
    color: var(--ink);
    font-size: 11.5px;
    line-height: 15.5px;
    font-style: normal;
  }
  .contacts {
    position: absolute; left: 15px; top: 187px;
    list-style: none;
    color: var(--ink);
    font-size: 11.5px;
  }
  .contacts li {
    display: flex; align-items: center; gap: 5px;
    height: 17px;
  }
  .contacts svg { width: 9px; height: 9px; flex: none; }
</style>
</head>
<body>
  <section class="card card--front">
    <div class="brand-name"><span class="mark"></span>Velmarine</div>
    <h2 class="company">Velmarine, LDA</h2>
    <address class="address">
      Rua das Oficinas, 42<br>
      Postal code: 1900-318 Lisboa
    </address>
    <ul class="contacts">
      <li>
        <svg viewBox="0 0 10 10" aria-hidden="true"><path d="M2 0.8 L3.6 2.8 L2.8 3.8 Q3.8 5.8 6.2 7.2 L7.2 6.4 L9.2 8 L8 9.4 Q4.6 9.2 2.2 6.4 Q0.6 4.2 0.6 2 Z" fill="#1e9bd7"/></svg>
        +351 214507382
      </li>
      <li>
        <svg viewBox="0 0 10 10" aria-hidden="true"><rect x="0" y="1.5" width="10" height="7" fill="#1e9bd7"/><path d="M0.5 2 L5 5.6 L9.5 2" stroke="#fff" stroke-width="1" fill="none"/></svg>
        velmarine.mail@postmail.pt
      </li>
      <li>
        <svg viewBox="0 0 10 10" aria-hidden="true"><rect x="0" y="0" width="10" height="10" rx="1.5" fill="#1e9bd7"/></svg>
        www.velmarine-auto.pt
      </li>
    </ul>
  </section>

  <section class="card card--back">
    <div class="brand-name"><span class="mark"></span>Velmarine</div>
  </section>
</body>
</html>
```